We need a PowerPoint to outline what Modeling is about!

PowerPoint presentation to be shown to aspiring models. The students will be joining our 1-day workshop, and they will be taught the very basics of being a model.
What should be included in the slides:
• What is Modelling? - Description of Modelling, and what it takes to be a Model.
• Types of Models in the market - Catwalk Model / Photography Model / Events Model
• Expectations of a model - Professionalism, Punctuality, Confidence, etc etc.
• Practical (catwalk) tips: Posture
• Practical (catwalk) tips: How to do a simple catwalk
• Practical (photography) tips: How to bring out your best angles in photos
• Trainer Assessment of Students
Here are some definitions that we use. You may change the wording as you see fit, as long as the meaning is the same.
Modelling is to promote a product / brand / service in an advertisement, show, commercial or event.
Runway / Fashion Model – Walk the catwalk to promote clothing and accessories in a fashion show.
Most shows require the model to be tall and skinny. Model needs to strut with confidence and grace down the runway. Body shape more important than facial features.
Photography Model – Appear for Print Ads, Magazine Editorials, Posters, etc.
Height requirements are not as strict (or not present) as compared to Runway Model. Good features preferred, but not a must.
Video Model – Appear for TV commercials, Promotional Videos, etc.
Model needs to possess basic acting skills to promote the product, brand or service on video. Confidence and screen charisma more important than looks or body.
Events Model – Promote the product, brand or service during ‘live’ events and shows.
Model needs to be engaging and charismatic to ‘sell’ the product to customers.
A longer description can also be found here: http://www.brightlarkagency.sg/models/
Target Market(s)
Adults aged 18 - 40 who are interested to take up Modeling.
Industry/Entity Type
Events
Requirements
Must have
- Visually appealing! Does not have to be content heavy, but should deliver the message effectively.
Nice to have
- Pretty pictures.

```html
<!DOCTYPE html>
<html lang="en">
<head>
<meta charset="utf-8">
<title>Bright Lark Studio – Modelling Workshop Slides</title>
<link rel="stylesheet" href="https://fonts.googleapis.com/css2?family=Open+Sans:wght@400;700&display=swap">
<style>
  :root {
    --stage: #2b2b2b;
    --slide: #ffffff;
    --ink: #333333;
    --ink-soft: #3a3a3a;
    --rule: #b5b5b5;
    --header: #333333;
    --header-edge: #8a8a8a;
    --header-text: #ffffff;
    --photo-left-a: #1a1a1a;
    --photo-left-b: #8c8c8c;
    --photo-right-a: #2a2a2a;
    --photo-right-b: #6e6e6e;
  }
  * { margin: 0; padding: 0; box-sizing: border-box; }
  html, body { width: 1200px; height: 1000px; overflow: hidden; }
  body {
    background: var(--stage);
    font-family: "Open Sans", Verdana, sans-serif;
    color: var(--ink);
    position: relative;
  }
  .slide {
    position: absolute;
    background: var(--slide);
    overflow: hidden;
  }
  /* Title slide */
  .slide--title { left: 11px; top: 15px; width: 657px; height: 493px; }
  .portrait { position: absolute; top: 0; height: 277px; }
  .portrait--left {
    left: 0; width: 254px;
    background: radial-gradient(ellipse at 50% 45%, var(--photo-left-b) 0%, #555 35%, var(--photo-left-a) 75%);
  }
  .portrait--right {
    left: 422px; width: 235px;
    background: radial-gradient(ellipse at 40% 40%, var(--photo-right-b) 0%, #444 40%, var(--photo-right-a) 80%);
  }
  .rule-pair {
    position: absolute; height: 6px;
    border-top: 2px solid var(--rule);
    border-bottom: 1px solid var(--rule);
  }
  .slide--title .rule-pair--left { left: 0; top: 318px; width: 254px; }
  .slide--title .rule-pair--right { left: 421px; top: 318px; width: 236px; }
  .brand {
    position: absolute;
    display: flex; flex-direction: column; align-items: center; justify-content: center;
    gap: 8px;
    color: var(--ink);
    font-weight: 700;
    text-align: center;
    line-height: 1.1;
    letter-spacing: 1px;
  }
  .brand__mark { background: var(--ink); display: block; }
  .slide--title .brand { left: 270px; top: 235px; width: 140px; height: 140px; font-size: 20px; }
  .slide--title .brand__mark { width: 26px; height: 26px; }
  .slide-title {
    position: absolute; left: 0; right: 0; top: 383px;
    text-align: center;
    font-size: 45px; font-weight: 400;
    color: var(--ink-soft);
    letter-spacing: 1px;
  }
  /* Content slide */
  .slide--content { left: 523px; top: 493px; width: 657px; height: 492px; }
  .slide-header {
    position: absolute; left: 0; top: 0; width: 100%; height: 56px;
    background: var(--header);
    border-bottom: 3px solid var(--header-edge);
    color: var(--header-text);
    font-size: 25px; font-weight: 400;
    padding: 11px 0 0 10px;
    letter-spacing: 0.3px;
  }
  .model-type {
    position: absolute; left: 29px; top: 110px; width: 610px;
    font-size: 24px; line-height: 1.35; color: var(--ink);
  }
  .model-type strong { font-weight: 700; }
  .model-note {
    position: absolute; left: 34px; top: 212px; width: 600px;
    font-family: Verdana, "Open Sans", sans-serif;
    font-size: 17px; line-height: 1.3; color: var(--ink);
  }
  .slide--content .rule-pair--left { left: 0; top: 434px; width: 280px; }
  .slide--content .rule-pair--right { left: 380px; top: 434px; width: 277px; }
  .slide--content .brand { left: 286px; top: 410px; width: 88px; height: 82px; font-size: 12px; gap: 5px; }
  .slide--content .brand__mark { width: 14px; height: 14px; }
</style>
</head>
<body>
  <section class="slide slide--title">
    <div class="portrait portrait--left" role="img" aria-label="Black and white portrait of a female model in a white lace top"></div>
    <div class="portrait portrait--right" role="img" aria-label="Black and white portrait of a male model in a suit and skinny tie"></div>
    <div class="rule-pair rule-pair--left"></div>
    <div class="rule-pair rule-pair--right"></div>
    <div class="brand">
      <span class="brand__mark"></span>
      <span class="brand__name">BRIGHT LARK<br>STUDIO</span>
    </div>
    <h1 class="slide-title">PRESENTATION</h1>
  </section>

  <section class="slide slide--content">
    <h2 class="slide-header">TYPES OF THE MODELS IN THE MARKET</h2>
    <p class="model-type"><strong>Photography Model</strong> – Appear for Print Ads, Magazine Editorials, Posters, etc.</p>
    <p class="model-note">Height requirements are not as strict (or not present) as compared to Runway Model. Good features preferred, but not a must.</p>
    <div class="rule-pair rule-pair--left"></div>
    <div class="rule-pair rule-pair--right"></div>
    <div class="brand">
      <span class="brand__mark"></span>
      <span class="brand__name">BRIGHT LARK<br>STUDIO</span>
    </div>
  </section>
</body>
</html>
```